Soccer Photo Poster

I am needing posters to put put 4 to 6 photos into the design. Each poster will represent a soccer player for the state tournament. The photos will be action shots that have been taken throughout the year. I would like to have the players #, player name and the photos to be something that I can change out on my own.

Attached is the theme this year of splatter paint so you can work with that as a base but hopefully come up with something a lot better!!

This is a full size poster!! It will be placed on the hotel doors for each player (2 for per room).
Updates

I just updated the team logo and the senior splatter paint that all the bags and T-shirts are being done in. I do not want them identical to this but just something that will look good next to or along with all the other items ordered or made.

 
please feel free post questions.

Here is something that I liked from another designer. This might give some direction for the project..

 It, sorry for the confusion.The Comets soccer attachment is the correct way to sppell

Target Market(s)

Girls high school soccer team. The school name is the Rapid City Halvorsen Comets and the colors are blue and white but the senior theme is "splatter paint".

Industry/Entity Type

Paint

Requirements
Must have
• Space (frames?) for 4 to 6 photos
Space (frame?) for player name, player #
Halvorsen Comets 2013

```html
<!DOCTYPE html>
<html lang="en">
<head>
<meta charset="utf-8">
<title>Soccer Player Poster – Halvorsen Comets 2013</title>
<link rel="stylesheet" href="https://fonts.googleapis.com/css2?family=Poppins:wght@500;600&family=Questrial&display=swap">
<style>
  :root {
    --grass-deep: #1c4d16;
    --grass: #2f7a24;
    --grass-light: #4f9a2c;
    --splat-yellow: #e9d91f;
    --splat-teal: #2fd09a;
    --splat-dark: #0f3d22;
    --frame-shade: rgba(20, 70, 55, 0.85);
    --frame-olive: rgba(95, 100, 40, 0.85);
    --photo: #ffffff;
    --title-yellow: #efe021;
    --number-teal: #2ecf97;
    --rule: rgba(255, 255, 255, 0.85);
  }
  * { margin: 0; padding: 0; box-sizing: border-box; }
  html, body { width: 900px; height: 1200px; overflow: hidden; background: #ffffff; }
  .poster {
    position: relative;
    width: 900px;
    height: 1200px;
    overflow: hidden;
    font-family: "Questrial", "Century Gothic", sans-serif;
  }
  .backdrop {
    position: absolute;
    inset: 0;
    background:
      radial-gradient(ellipse 260px 340px at 150px 470px, rgba(233,217,31,0.9), rgba(233,217,31,0) 70%),
      radial-gradient(ellipse 220px 260px at 430px 300px, rgba(233,217,31,0.75), rgba(233,217,31,0) 70%),
      radial-gradient(ellipse 320px 240px at 420px 720px, rgba(47,208,154,0.85), rgba(47,208,154,0) 70%),
      radial-gradient(ellipse 200px 200px at 110px 780px, rgba(47,208,154,0.7), rgba(47,208,154,0) 70%),
      radial-gradient(ellipse 260px 200px at 800px 720px, rgba(47,208,154,0.7), rgba(47,208,154,0) 70%),
      radial-gradient(ellipse 300px 260px at 560px 240px, rgba(47,208,154,0.6), rgba(47,208,154,0) 70%),
      radial-gradient(ellipse 180px 260px at 470px 1000px, rgba(233,217,31,0.55), rgba(233,217,31,0) 70%),
      linear-gradient(160deg, var(--grass-deep) 0%, var(--grass) 45%, var(--grass-light) 70%, var(--grass-deep) 100%);
  }
  .frame-shade, .photo { position: absolute; }
  .frame-shade { background: var(--frame-shade); }
  .frame-shade.olive { background: var(--frame-olive); }
  .photo { background: var(--photo); }

  .number {
    position: absolute;
    left: 44px;
    top: 268px;
    font-family: "Poppins", "Century Gothic", sans-serif;
    font-weight: 500;
    font-size: 330px;
    line-height: 1;
    letter-spacing: -18px;
    color: var(--number-teal);
    text-shadow: 6px 8px 14px rgba(0, 40, 20, 0.55);
  }
  .rule {
    position: absolute;
    left: 78px;
    top: 642px;
    width: 738px;
    height: 1px;
    background: var(--rule);
  }
  .player-title {
    position: absolute;
    left: 0;
    top: 652px;
    width: 900px;
    text-align: center;
    font-size: 86px;
    line-height: 1.1;
    color: var(--title-yellow);
    text-shadow: 4px 6px 10px rgba(0, 40, 20, 0.6);
  }
  .team-mark {
    position: absolute;
    left: 370px;
    top: 852px;
    width: 186px;
    display: flex;
    flex-direction: column;
    align-items: center;
    gap: 10px;
  }
  .team-mark .dot {
    width: 40px;
    height: 40px;
    border-radius: 50%;
    background: var(--title-yellow);
  }
  .team-mark .name {
    font-size: 26px;
    line-height: 1.1;
    text-align: center;
    color: var(--title-yellow);
  }
  .season {
    position: absolute;
    left: 361px;
    top: 1054px;
    width: 200px;
    text-align: center;
    font-family: "Poppins", "Century Gothic", sans-serif;
    font-weight: 600;
    font-size: 36px;
    line-height: 1.05;
    color: var(--title-yellow);
  }
</style>
</head>
<body>
<main class="poster">
  <div class="backdrop" role="img" aria-label="Grass field covered in yellow, teal and green splatter paint"></div>

  <!-- top row of action photos -->
  <div class="frame-shade olive" style="left:0;top:72px;width:300px;height:190px;transform:rotate(-3deg);"></div>
  <div class="photo top-photo" role="img" aria-label="Player action photo" style="left:20px;top:78px;width:280px;height:172px;transform:rotate(-3deg);"></div>

  <div class="frame-shade" style="left:292px;top:40px;width:302px;height:190px;transform:rotate(-3deg);"></div>
  <div class="photo top-photo" role="img" aria-label="Player action photo" style="left:312px;top:52px;width:280px;height:170px;transform:rotate(-3deg);"></div>

  <div class="frame-shade" style="left:582px;top:10px;width:302px;height:190px;transform:rotate(-3deg);"></div>
  <div class="photo top-photo" role="img" aria-label="Player action photo" style="left:602px;top:22px;width:280px;height:170px;transform:rotate(-3deg);"></div>

  <!-- feature photo -->
  <div class="frame-shade olive" style="left:386px;top:248px;width:470px;height:348px;"></div>
  <div class="photo feature-photo" role="img" aria-label="Player portrait photo" style="left:406px;top:270px;width:452px;height:330px;"></div>

  <div class="number">10</div>

  <div class="rule"></div>
  <h1 class="player-title">SOCCER PLAYER</h1>

  <!-- bottom photos -->
  <div class="frame-shade" style="left:0;top:808px;width:320px;height:370px;transform:rotate(-4deg);"></div>
  <div class="photo bottom-photo" role="img" aria-label="Player action photo" style="left:26px;top:830px;width:316px;height:354px;transform:rotate(-4deg);"></div>

  <div class="frame-shade" style="left:610px;top:760px;width:320px;height:380px;transform:rotate(5deg);"></div>
  <div class="photo bottom-photo" role="img" aria-label="Player action photo" style="left:594px;top:784px;width:316px;height:370px;transform:rotate(5deg);"></div>

  <div class="team-mark">
    <span class="dot"></span>
    <span class="name">HALVORSEN<br>COMETS</span>
  </div>

  <p class="season">HALVORSEN<br>COMETS<br>2013</p>
</main>
</body>
</html>
```